Introduction of new dentist and new treatments

We want inform our Patients of our new dentist and new treatment methods. It is dealing about biologic dentistry and holistic dentistry. we are in switzerland and speak german

Font styles to use
Sans Serif

Colors
00a990
33b8a4
9bcb3c
acd036
cadf82
0292cd
3176b5
e34297
e667a6

Requirements
Must have
• Text, which can be edited. It will be in german
• Name of the dental clinic is
• "Brivana - Ihr Zahnarzt in Zug"
Nice to have
• A4 Layout

```html
<!DOCTYPE html>
<html lang="de">
<head>
<meta charset="utf-8">
<title>Brivana – Interdisziplinäre Zahnmedizin</title>
<link href="https://fonts.googleapis.com/css2?family=Arimo:wght@400;700&display=swap" rel="stylesheet">
<style>
:root{
  --bg:#ececec;
  --paper:#ffffff;
  --green:#4fba58;
  --blue:#1172bd;
  --sky:#2aa8e0;
  --pink:#f08ca0;
  --navy:#25366b;
  --ink:#1d1d1d;
}
*{margin:0;padding:0;box-sizing:border-box}
html,body{width:1200px;height:1200px;overflow:hidden;background:var(--bg)}
body{font-family:"Arimo",Arial,sans-serif;color:var(--ink);position:relative}
.flyer{position:absolute;left:266px;top:128px;width:835px;height:1183px;background:var(--paper);transform:scale(.8);transform-origin:0 0;overflow:hidden}
.header-band{position:absolute;left:0;top:0;width:835px;height:236px;background:var(--green);clip-path:polygon(0 0,100% 0,100% 160px,0 236px)}
.header-rule{position:absolute;left:0;top:244px;width:835px;height:6px;background:var(--sky);clip-path:polygon(0 0,100% 0,100% 100%,0 100%);transform:skewY(-5.2deg);transform-origin:100% 0}
.portrait{position:absolute;left:160px;top:30px;width:185px;height:200px;border-radius:90px 90px 0 0;background:linear-gradient(180deg,#e8c2a8 0%,#d9a98c 55%,#1d6fc0 80%,#1565b5 100%)}
.brand{position:absolute;left:470px;top:46px;width:320px;text-align:center;color:var(--navy)}
.brand-name{font-size:36px;letter-spacing:9px;font-weight:400;display:flex;align-items:center;justify-content:center;gap:14px}
.brand-name .dot{width:14px;height:14px;border-radius:50%;background:var(--navy)}
.brand-tag{font-size:17px;margin-top:10px}
.title{position:absolute;right:38px;top:252px;text-align:right;color:var(--blue);font-weight:700;font-size:23.5px;line-height:31px;letter-spacing:.2px}
.intro{position:absolute;left:0;top:350px;width:815px;height:87px;background:var(--pink);clip-path:polygon(55px 0,100% 0,100% 100%,0 100%)}
.intro p{position:absolute;left:189px;top:12px;width:610px;color:#fff;font-size:16.4px;line-height:20px}
.col-head{position:absolute;left:20px;top:458px;color:var(--green);font-weight:700;font-size:18.5px;line-height:24px}
.body{font-size:15.2px;line-height:25.2px}
.col-left{position:absolute;left:20px;top:514px;width:385px}
.box-blue{position:absolute;left:416px;top:446px;width:399px;height:111px;background:var(--blue);clip-path:polygon(24px 0,100% 0,100% 100%,0 100%)}
.box-blue h2{position:absolute;left:50px;top:10px;color:#fff;font-size:24px;line-height:32.5px;font-weight:700}
.col-right{position:absolute;left:436px;top:564px;width:372px}
.col-right .accent{color:var(--blue)}
.band-green{position:absolute;left:0;top:846px;width:596px;height:56px;background:var(--green);clip-path:polygon(0 0,570px 0,100% 100%,0 100%)}
.band-green h2{position:absolute;left:29px;top:17px;color:#fff;font-size:18px;font-weight:700;letter-spacing:.3px}
.para{position:absolute;left:30px;width:770px;font-size:15.2px;line-height:19.8px}
.para-1{top:916px}
.band-pink{position:absolute;left:353px;top:996px;width:482px;height:46px;background:var(--pink);clip-path:polygon(20px 0,100% 0,100% 100%,0 100%)}
.band-pink h2{position:absolute;left:49px;top:10px;color:#fff;font-size:24px;font-weight:700}
.para-2{top:1055px}
</style>
</head>
<body>
<main class="flyer">
  <div class="header-band" aria-hidden="true"></div>
  <div class="portrait" role="img" aria-label="Porträtfoto des neuen Zahnarztes im blauen Poloshirt"></div>
  <div class="brand">
    <div class="brand-name"><span class="dot"></span>BRIVANA</div>
    <div class="brand-tag">Ihr Zahnarzt in Zug</div>
  </div>

  <h1 class="title">INTERDISZIPLINÄRE ZAHNMEDIZIN<br>ZUSAMMENHANG ZWISCHEN ZAHNPROBLEMEN<br>UND DER GESUNDHEIT VON KÖRPER UND GEIST</h1>

  <div class="intro"><p>Zahn und Gesundheit haben eins gemeinsam – Man vermisst sie, wenn sie fehlt. Zähne haben einen engen Zusammenhang zur Gesundheit und können diese beeinflussen. Sowohl negativ als auch positiv.</p></div>

  <h2 class="col-head">FUNKTION DES KAUORGANS<br>UND INTERDISZIPLINÄRE ZAHNMEDIZIN</h2>
  <p class="body col-left">“Funktion ist nicht alles. Aber ohne Funktion ist alles nichts!“ Sagte einst Prof. A. Hartmann (Zahnarzt, Gnathologie) und betonte die Bedeutung der Funktion des Kausystems. Sprechen, Kauen aber auch Körperhaltung und Stressmanagement gehören zu den Funktionen der Zähne. Ein gut funktionierendes Kauorgan (nach Prof. R. Lindner, interdisziplinäre Zahnmedizin) kann Stress bewältigen und mehr Leistung und Wohlbefinden bringen. Sehr oft erkennt man Funktionsstörungen daran, dass die Zähne nicht richtig zueinander passen oder Muskelverspannungen und Schmerzen im Kiefergelenk auftreten.</p>

  <div class="box-blue"><h2>PARODONTITIS<br>UND SYSTEMISCHE<br>ERKRANKUNGEN</h2></div>
  <p class="body col-right">Parodontitis (Entzündung des Zahnhalteapparats) ist eine der häufigsten chronischen Krankheiten weltweit und daher gut erforscht. Herzkrankheiten, Diabetes und Frühgeburtlichkeit sind einige der systemischen Krankheiten mit der Parodontitis in Zusammenhang steht. <span class="accent">Zahnfleischbluten, Zahnlockerung, Zahnfleischschwund und Zahnverlust sind typische Begleiterscheinungen von Parodontitis.</span> Eine systematische Parodontitis-Behandlung kann auch positive Auswirkungen auf die gesamte Gesundheit haben.</p>

  <div class="band-green"><h2>ZAHNVERLUST UND NEUROLOGISCHE AUSWIRKUNG</h2></div>
  <p class="para para-1">Ein physiologisches Kausystem hat sehr feine Steuerungs- und Wahrnehmungsmöglichkeiten. Bei Zahnverlust werden diese Fähigkeiten weniger benötigt. Weniger gebrauchte Ressourcen werden von der Natur dementsprechend abgebaut. Studien zeigen, dass Menschen mit weniger Zähnen mehr Risiko zur Bildung von Demenz bergen.</p>

  <div class="band-pink"><h2>GANZHEITLICHE ERKLÄRUNGEN</h2></div>
  <p class="para para-2">Die komplementäre Zahnheilkunde, sehr oft auch als ganzheitliche oder biologische Zahnheilkunde bezeichnet, versucht mit Hilfe von Meridianen (Traditionelle Chinesische Medizin), den Zusammenhang zwischen Zähnen und anderen Organen und Körperteilen zu erklären. Es gibt immer mehr Patienten und Zahnärzte die von dieser Theorie und deren Ergebnissen überzeugt sind. Aufgrund der wissenschaftlichen Lage ist eine ausführliche Aufklärung vor der Behandlung sehr ratsam.</p>
</main>
</body>
</html>
```